Business card design for Automotive workshop

We need a business card for a new automotive repair and tyre shop called Ridgeback Prime Automotive located in New Zealand. We are a clean, modern and fresh workshop and company.

Front needs to feature logo,
my name:
Lachie Westergaard (director)

Address:
48 Marlow Lane
Kauri Bay 3597

Phone: 07 842 1937
Mobile: 027 519 2764
Email: office@ridgebackmotors.co.nz
Website: ridgebackmotors.co.nz

Back needs to feature an area to write down appointment details, date and time.

Also feature a list of jobs and work we do such as,
Vehicle Servicing
All Mechanical Repairs
Warrant of Fitness
Tyres & Wheel Alignments
Automotive Diagnostics
Automotive Parts & Supplies

```html
<!DOCTYPE html>
<html lang="en">
<head>
<meta charset="utf-8">
<title>Ridgeback Prime Automotive – Business Card</title>
<link href="https://fonts.googleapis.com/css2?family=Open+Sans:wght@400;600;700;800&display=swap" rel="stylesheet">
<style>
  :root{
    --stage:#2b2826;
    --card:#111111;
    --panel:#333333;
    --red:#e31b23;
    --white:#ffffff;
    --rule:#8a8a8a;
  }
  *{box-sizing:border-box;margin:0;padding:0}
  html,body{width:1200px;height:795px;overflow:hidden}
  body{background:var(--stage);font-family:"Open Sans",Arial,sans-serif;color:var(--white);position:relative}
  .card{position:absolute;top:242px;width:540px;height:310px;background:var(--card);overflow:hidden;box-shadow:0 10px 30px rgba(0,0,0,.45)}
  .card--back{left:40px}
  .card--front{left:620px;border-left:4px solid var(--red);border-bottom:4px solid var(--red)}

  /* back */
  .write-area{position:absolute;top:22px;left:110px;right:26px;height:150px;background:var(--panel)}
  .appt-title{position:absolute;top:30px;left:110px;right:26px;text-align:center;color:var(--red);font-weight:700;font-size:20px;letter-spacing:.3px}
  .field{position:absolute;display:flex;align-items:flex-end;gap:8px;font-size:14px;font-weight:600}
  .field__line{flex:1;border-bottom:1.5px dashed var(--white);height:1px;margin-bottom:4px}
  .field--date{top:92px;left:26px;right:290px}
  .field--time{top:142px;left:250px;right:40px}
  .works{position:absolute;left:0;right:0;bottom:0;height:110px;background:var(--red)}
  .works__pill{position:absolute;top:-16px;left:50%;transform:translateX(-50%);background:var(--red);border:2px solid var(--card);border-radius:16px;padding:3px 26px;font-weight:700;font-size:15px;white-space:nowrap}
  .works__list{position:absolute;top:28px;left:18px;right:18px;display:flex;flex-wrap:wrap;justify-content:center;gap:8px 14px;font-size:13px;list-style:none}
  .works__list li::before{content:"•";margin-right:5px}

  /* front */
  .brand{position:absolute;top:44px;right:40px;text-align:right;color:var(--red);font-weight:800;font-size:30px;line-height:1.05;text-transform:uppercase;letter-spacing:1px}
  .brand span{display:block;font-size:17px;letter-spacing:4px}
  .person{position:absolute;top:158px;left:30px;width:200px;text-align:right}
  .person__name{color:var(--red);font-weight:700;font-size:19px;line-height:1.2;white-space:nowrap}
  .person__role,.person__addr{font-size:13.5px;line-height:1.45}
  .person__role{margin-bottom:2px}
  .divider{position:absolute;top:192px;left:246px;width:1px;height:92px;background:var(--rule)}
  .contact{position:absolute;top:192px;left:262px;list-style:none;font-size:13.5px;line-height:1.65}
  .contact li{display:flex;align-items:center;gap:8px}
  .contact svg{width:12px;height:12px;fill:var(--red);flex:none}
</style>
</head>
<body>

<section class="card card--back" aria-label="Card back">
  <div class="write-area"></div>
  <h2 class="appt-title">Appointment Details</h2>
  <div class="field field--date"><span>Date</span><span class="field__line"></span></div>
  <div class="field field--time"><span>Time</span><span class="field__line"></span></div>
  <div class="works">
    <div class="works__pill">Our Works</div>
    <ul class="works__list">
      <li>Vehicle Servicing</li>
      <li>Warrant of Fitness</li>
      <li>Automotive Parts &amp; Supplies</li>
      <li>Automotive Diagnostics</li>
      <li>Tyres &amp; Wheel Alignments</li>
      <li>All Mechanical Repairs</li>
    </ul>
  </div>
</section>

<section class="card card--front" aria-label="Card front">
  <div class="brand">Ridgeback Prime<span>Automotive</span></div>
  <div class="person">
    <div class="person__name">Lachie Westergaard</div>
    <div class="person__role">Director</div>
    <div class="person__addr">48 Marlow Lane<br>Kauri Bay 3597</div>
  </div>
  <div class="divider"></div>
  <ul class="contact">
    <li><svg viewBox="0 0 24 24"><path d="M6.6 10.8a15 15 0 0 0 6.6 6.6l2.2-2.2c.3-.3.7-.4 1-.2 1.1.4 2.3.6 3.6.6.6 0 1 .4 1 1V20c0 .6-.4 1-1 1A17 17 0 0 1 3 4c0-.6.4-1 1-1h3.5c.6 0 1 .4 1 1 0 1.3.2 2.5.6 3.6.1.3 0 .7-.2 1z"/></svg>07 842 1937</li>
    <li><svg viewBox="0 0 24 24"><path d="M7 1h10a2 2 0 0 1 2 2v18a2 2 0 0 1-2 2H7a2 2 0 0 1-2-2V3a2 2 0 0 1 2-2zm0 3v14h10V4zm5 15.5a1 1 0 1 0 0 2 1 1 0 0 0 0-2z"/></svg>027 519 2764</li>
    <li><svg viewBox="0 0 24 24"><path d="M2 5h20v14H2zm2 2v.5l8 5 8-5V7zm0 3v7h16v-7l-8 5z"/></svg>office@ridgebackmotors.co.nz</li>
    <li><svg viewBox="0 0 24 24"><path d="M12 2a10 10 0 1 0 0 20 10 10 0 0 0 0-20zm6.9 6h-3a15 15 0 0 0-1.3-4A8 8 0 0 1 18.9 8zM12 4c.8 1.2 1.5 2.5 1.9 4h-3.8c.4-1.5 1.1-2.8 1.9-4zM4.3 14a8 8 0 0 1 0-4h3.4a16 16 0 0 0 0 4zm.8 2h3a15 15 0 0 0 1.3 4A8 8 0 0 1 5.1 16zm3-8h-3a8 8 0 0 1 4.3-4 15 15 0 0 0-1.3 4zM12 20c-.8-1.2-1.5-2.5-1.9-4h3.8c-.4 1.5-1.1 2.8-1.9 4zm2.3-6H9.7a14 14 0 0 1 0-4h4.6a14 14 0 0 1 0 4zm.3 6a15 15 0 0 0 1.3-4h3a8 8 0 0 1-4.3 4zm1.7-6a16 16 0 0 0 0-4h3.4a8 8 0 0 1 0 4z"/></svg>ridgebackmotors.co.nz</li>
  </ul>
</section>

</body>
</html>
```